Label design for olive oil and other oils

We are a company located in Melbourne, doing the international trade, now we are starting a olive oil project and need a label for our product. Our olive oil named "Blue Heron", our products is produce in Australia and will export oversea, The label should be brief and clear. We offer the natural and premium products to our customers. The bottles of the oil will be 500ml, 750ml and 1L. Our label will use for other kinds of oil in the future, such as the nut oil, almond oil and macadamia oil, so we would like the design can be expand to other oil as well, so a series of oil label will be welcomed.

Australia local market and oversea.

Food Store

• The blue heron bird

```html
<!DOCTYPE html>
<html lang="en">
<head>
<meta charset="utf-8">
<title>Blue Heron Olive Oil Label</title>
<link rel="stylesheet" href="https://fonts.googleapis.com/css2?family=Poiret+One&display=swap">
<style>
  :root {
    --page: #ffffff;
    --label-black: #0b0b0b;
    --label-edge: #f2f2f2;
    --gold-light: #fbe7a1;
    --gold: #d9a93a;
    --gold-dark: #9a6a12;
    --ink-light: #f4f4f4;
    --leaf-light: #a8c83c;
    --leaf-mid: #5f8d22;
    --leaf-dark: #2f5216;
    --heron-sky: #eef0ee;
    --heron-soft: #b9c3cf;
  }
  html, body {
    margin: 0;
    padding: 0;
    width: 1200px;
    height: 4152px;
    overflow: hidden;
    background: var(--page);
  }
  .label {
    position: relative;
    width: 1200px;
    height: 4152px;
  }
  .label-shape {
    position: absolute;
    inset: 0;
  }
  .brand-name {
    position: absolute;
    left: 0;
    width: 1200px;
    top: 1196px;
    margin: 0;
    text-align: center;
    font-family: "Poiret One", sans-serif;
    font-weight: 400;
    font-size: 100px;
    line-height: 1;
    color: var(--gold-light);
  }
  .copy-line {
    position: absolute;
    left: 0;
    width: 1200px;
    margin: 0;
    text-align: center;
    font-family: "Poiret One", sans-serif;
    font-weight: 400;
    line-height: 1;
    color: var(--ink-light);
    text-transform: uppercase;
  }
  .line-natural { top: 2740px; font-size: 112px; letter-spacing: 2px; }
  .line-organic { top: 2862px; font-size: 92px; }
  .line-virgin  { top: 2968px; font-size: 84px; }
  .divider {
    position: absolute;
    left: 350px;
    top: 3108px;
  }
  .line-olive-oil { top: 3180px; font-size: 124px; }
  .volume { top: 3775px; font-size: 62px; letter-spacing: 4px; text-transform: none; }
</style>
</head>
<body>
<main class="label">
  <svg class="label-shape" width="1200" height="4152" viewBox="0 0 1200 4152">
    <defs>
      <linearGradient id="gold-frame" x1="0" y1="0" x2="1" y2="0">
        <stop offset="0" stop-color="var(--gold-dark)"/>
        <stop offset="0.25" stop-color="var(--gold-light)"/>
        <stop offset="0.5" stop-color="var(--gold)"/>
        <stop offset="0.75" stop-color="var(--gold-light)"/>
        <stop offset="1" stop-color="var(--gold-dark)"/>
      </linearGradient>
      <radialGradient id="heron-tone" cx="0.5" cy="0.45" r="0.6">
        <stop offset="0" stop-color="var(--heron-soft)"/>
        <stop offset="1" stop-color="var(--heron-sky)"/>
      </radialGradient>
      <radialGradient id="branch-tone" cx="0.5" cy="0.45" r="0.5">
        <stop offset="0" stop-color="var(--leaf-light)"/>
        <stop offset="0.55" stop-color="var(--leaf-mid)" stop-opacity="0.8"/>
        <stop offset="1" stop-color="var(--leaf-dark)" stop-opacity="0"/>
      </radialGradient>
    </defs>

    <path class="label-body"
          d="M30 300 Q30 200 110 180 Q175 165 195 110 Q220 20 600 20 Q980 20 1005 110 Q1025 165 1090 180 Q1170 200 1170 300 L1170 4070 Q1170 4130 1110 4130 L90 4130 Q30 4130 30 4070 Z"
          fill="var(--label-black)" stroke="var(--label-edge)" stroke-width="8"/>

    <path class="label-frame"
          d="M80 330 Q80 250 140 236 Q220 215 245 150 Q270 75 600 75 Q930 75 955 150 Q980 215 1060 236 Q1120 250 1120 330 L1120 4030 Q1120 4075 1075 4075 L125 4075 Q80 4075 80 4030 Z"
          fill="none" stroke="url(#gold-frame)" stroke-width="16"/>

    <circle class="heron-medallion" role="img" aria-label="Illustration of a blue heron bird inside the brand medallion"
            cx="604" cy="880" r="300"
            fill="url(#heron-tone)" stroke="url(#gold-frame)" stroke-width="24"/>

    <ellipse class="olive-branch" role="img" aria-label="Illustration of an olive branch with green olives and leaves"
             cx="600" cy="1620" rx="400" ry="360" fill="url(#branch-tone)"/>
  </svg>

  <p class="brand-name">Blue Heron</p>

  <p class="copy-line line-natural">Natural</p>
  <p class="copy-line line-organic">Organic</p>
  <p class="copy-line line-virgin">Extra Virgin</p>
  <svg class="divider" width="500" height="30" viewBox="0 0 500 30">
    <line x1="0" y1="15" x2="225" y2="15" stroke="var(--ink-light)" stroke-width="4"/>
    <rect x="238" y="3" width="17" height="17" transform="rotate(45 246 12)" fill="none" stroke="var(--ink-light)" stroke-width="4"/>
    <line x1="275" y1="15" x2="500" y2="15" stroke="var(--ink-light)" stroke-width="4"/>
  </svg>
  <p class="copy-line line-olive-oil">Olive Oil</p>

  <p class="copy-line volume">1000 ml</p>
</main>
</body>
</html>
```